Personal Trainer and Corporate Health Business

I need a business card for a new company I'm starting in Australia called "Brisk Vitality Partners" I will be providing a Personal training service as well as corporate health in companies.
The service provided is to help promote an active and healthy lifstyle.
The design should communicate a healthy lifestyle and also the benefits that this can have on a personal level and in the corporate environment and the benefits that flow from that.

Target Market(s)

Members of the public and Corporate

Industry/Entity Type

Environment

Requirements
Must have
• Company logo attached
Look and feel fresh and modern

Tag line: "Actively promoting a healthier lifestyle"

Lewis Norgate
Managing Director

m: 0417 596 304
e: lewis@briskvitalitypartners.com.au

www.briskvitalitypartners.com.au
Nice to have
• Can be 1 or 2 sided

```html
<!DOCTYPE html>
<html lang="en">
<head>
<meta charset="utf-8">
<title>Brisk Vitality Partners – Business Card</title>
<link rel="stylesheet" href="https://fonts.googleapis.com/css2?family=Noto+Serif:ital,wght@0,400;0,700;1,400;1,700&display=swap">
<style>
  :root {
    --backdrop: #ecebe7;
    --card: #ffffff;
    --brand-blue: #1d5ca6;
    --brand-green: #8dc03a;
    --card-shadow: rgba(0, 0, 0, 0.28);
  }
  * { margin: 0; padding: 0; box-sizing: border-box; }
  html, body {
    width: 1200px;
    height: 1000px;
    overflow: hidden;
    background: var(--backdrop);
    font-family: "Noto Serif", Georgia, serif;
  }
  .canvas { position: relative; width: 1200px; height: 1000px; }

  .card {
    position: absolute;
    width: 728px;
    height: 417px;
    background: var(--card);
    box-shadow: 4px 5px 10px var(--card-shadow);
  }
  .card--front { left: 53px; top: 83px; z-index: 2; }
  .card--back  { left: 402px; top: 420px; z-index: 1; }

  /* Front */
  .brand {
    position: absolute;
    left: 0;
    width: 728px;
    top: 188px;
    display: flex;
    justify-content: center;
    align-items: center;
    gap: 10px;
    padding-right: 90px;
  }
  .brand__dot {
    width: 14px;
    height: 14px;
    border-radius: 50%;
    background: var(--brand-green);
  }
  .brand__name {
    color: var(--brand-blue);
    font-size: 25px;
    font-weight: 700;
    letter-spacing: 0.5px;
  }
  .tagline {
    position: absolute;
    left: 152px;
    top: 252px;
    font-size: 21px;
    font-style: italic;
    letter-spacing: 0.6px;
    color: var(--brand-blue);
  }
  .tagline__accent { color: var(--brand-green); font-weight: 700; }

  /* Back */
  .person {
    position: absolute;
    right: 25px;
    top: 72px;
    text-align: left;
  }
  .person__name {
    color: var(--brand-blue);
    font-size: 28px;
    font-weight: 700;
    letter-spacing: 0.8px;
    line-height: 1.1;
  }
  .person__role {
    color: var(--brand-green);
    font-size: 16px;
    margin-top: 2px;
  }
  .contact {
    position: absolute;
    right: 37px;
    top: 274px;
    text-align: right;
    font-size: 15px;
    line-height: 24px;
    letter-spacing: 0.6px;
  }
  .contact__phone { color: var(--brand-green); font-weight: 700; }
  .contact__line { color: var(--brand-blue); }
</style>
</head>
<body>
  <main class="canvas">
    <section class="card card--front" aria-label="Business card front">
      <div class="brand">
        <span class="brand__dot"></span>
        <span class="brand__name">Brisk Vitality Partners</span>
      </div>
      <p class="tagline">Actively promoting a <span class="tagline__accent">healthier</span> lifestyle</p>
    </section>

    <section class="card card--back" aria-label="Business card back">
      <div class="person">
        <h1 class="person__name">LEWIS NORGATE</h1>
        <p class="person__role">Managing Director</p>
      </div>
      <div class="contact">
        <p class="contact__phone">0417 596 304</p>
        <p class="contact__line">lewis@briskvitalitypartners.com.au</p>
        <p class="contact__line">www.briskvitalitypartners.com.au</p>
      </div>
    </section>
  </main>
</body>
</html>
```